Business Card Design Project

I am a Homoeopath and would like a new business card which represents my clinic and how I work...My clinic Bramble Wellness is situated near Calloway forest, you can hear the lyrebirds calling all the time!
My work is holistic and deals with shifting energy in order to create balance within the body. There is a very strong spiritual element to my work.
I have uploaded my current card, As far as the actual details on the front and the back I would like these to remain in the same structure...

Target Market(s)

those looking for alternative health therapies... all of my patients are referred to me so I am not concerned about fitting into a mainstream box

Industry/Entity Type

Clinic

Requirements
Must have
• This card must not look corporate!
be creative and different

Nice to have
• I am picturing a tree of life with roots heading into the earth and on it is a white peacock, maybe a body of water and a full moon nearby?

```html
<!DOCTYPE html>
<html lang="en">
<head>
<meta charset="utf-8">
<title>Bramble Wellness – Business Card</title>
<link rel="stylesheet" href="https://fonts.googleapis.com/css2?family=Didact+Gothic&family=Arimo:ital,wght@0,400;0,700;1,400&display=swap">
<style>
  :root {
    --backdrop: #ece9ef;
    --plum-deep: #1e0b2c;
    --plum: #3d1756;
    --plum-bright: #6b3590;
    --silver-light: #f4f4f6;
    --silver: #d9d9de;
    --silver-dark: #b9b9c0;
    --ink: #2a0f3c;
    --white: #ffffff;
    --field: rgba(255,255,255,0.85);
  }
  * { box-sizing: border-box; margin: 0; padding: 0; }
  html, body {
    width: 1200px; height: 900px; overflow: hidden;
    background: var(--backdrop);
  }
  .canvas {
    position: relative; width: 1200px; height: 900px;
  }
  .card {
    position: absolute; top: 170px;
    width: 340px; height: 560px;
    border-radius: 26px; overflow: hidden;
    box-shadow: 0 12px 30px rgba(40,10,60,0.18);
  }
  /* Back: appointment side */
  .card-back {
    left: 200px;
    background: linear-gradient(160deg, var(--silver-light) 0%, var(--silver) 55%, var(--silver-dark) 100%);
  }
  .back-ornament {
    position: absolute; top: 20px; left: 50px; width: 270px; height: 160px;
    border-radius: 40% 60% 50% 50%;
    background: radial-gradient(ellipse at 60% 45%, rgba(255,255,255,0.9), rgba(200,200,208,0.35) 60%, rgba(200,200,208,0) 75%);
  }
  .appointment-title {
    position: absolute; top: 196px; left: 0; width: 100%;
    text-align: center;
    font-family: "Arimo", Arial, sans-serif; font-weight: 700;
    font-size: 19px; color: var(--ink);
  }
  .appointment-fields {
    position: absolute; top: 232px; left: 36px; width: 268px;
    display: flex; flex-direction: column; gap: 14px;
  }
  .appointment-field {
    height: 34px; background: var(--field);
    border: 1px solid rgba(255,255,255,0.9);
  }
  .back-brand {
    position: absolute; top: 418px; left: 0; width: 100%;
    text-align: center;
    font-family: "Didact Gothic", "Century Gothic", sans-serif;
    font-size: 21px; color: var(--plum);
  }
  .back-band {
    position: absolute; left: 0; bottom: 0; width: 100%; height: 94px;
    background: linear-gradient(90deg, var(--plum-deep), var(--plum) 45%, var(--plum-bright) 75%, var(--plum));
    color: var(--white); text-align: center;
    font-family: "Arimo", Arial, sans-serif; font-size: 17px; line-height: 1.3;
    padding-top: 22px;
  }
  /* Front: practitioner side */
  .card-front {
    left: 660px;
    background: linear-gradient(90deg, var(--plum-deep) 0%, var(--plum) 35%, var(--plum-bright) 65%, var(--plum) 85%, var(--plum-deep) 100%);
    color: var(--white); text-align: center;
  }
  .front-ornament {
    position: absolute; top: 60px; left: 60px; width: 220px; height: 160px;
    border-radius: 50% 50% 45% 45%;
    background: radial-gradient(ellipse at 50% 50%, rgba(235,235,240,0.55), rgba(220,220,230,0.18) 55%, rgba(220,220,230,0) 72%);
  }
  .front-brand {
    position: absolute; top: 236px; left: 0; width: 100%;
    font-family: "Didact Gothic", "Century Gothic", sans-serif;
    font-size: 25px; color: var(--white);
  }
  .practitioner {
    position: absolute; top: 336px; left: 0; width: 100%;
    font-family: "Arimo", Arial, sans-serif;
  }
  .practitioner-name { font-weight: 700; font-size: 19px; margin-bottom: 4px; }
  .practitioner-role { font-style: italic; font-size: 13.5px; line-height: 1.35; }
  .practitioner-credentials { font-size: 13.5px; line-height: 1.35; }
  .contact {
    position: absolute; top: 414px; left: 0; width: 100%;
    font-family: "Arimo", Arial, sans-serif; font-size: 16px; line-height: 1.3;
  }
  .contact-phone { font-weight: 700; }
</style>
</head>
<body>
<main class="canvas">
  <section class="card card-back" aria-label="Card back – appointment reminder">
    <div class="back-ornament" role="img" aria-label="Faint silver flourish ornament"></div>
    <h2 class="appointment-title">Your next appointment</h2>
    <div class="appointment-fields">
      <div class="appointment-field"></div>
      <div class="appointment-field"></div>
      <div class="appointment-field"></div>
    </div>
    <p class="back-brand">Bramble Wellness</p>
    <div class="back-band">
      <p>48 Fernleigh Road, Kalmore.</p>
      <p>03 5712 4409</p>
    </div>
  </section>

  <section class="card card-front" aria-label="Card front – practitioner details">
    <div class="front-ornament" role="img" aria-label="Silver floral swirl ornament"></div>
    <h1 class="front-brand">Bramble Wellness</h1>
    <div class="practitioner">
      <p class="practitioner-name">Maren Holloway</p>
      <p class="practitioner-role">Classical Homeopath</p>
      <p class="practitioner-credentials">Ad Dip Hom Prof Memb AHA Aroh Regd</p>
    </div>
    <div class="contact">
      <p class="contact-email">maren_holloway@fernmail.com</p>
      <p class="contact-phone">0428 317 905</p>
    </div>
  </section>
</main>
</body>
</html>
```